Gobo Flyer to generate sales and to use at trade shows or as a leave behind to client

We are looking to create a flyer to promote our new exterior or interior event lighting options. We are looking for the layout to be clean and consistent with our color scheme. We are a professional technologically advanced company looking to take your event to the next level. We are looking for a layout which has an image at the top as well as a few other images to allow reader to see a few options

Target Market(s)

Residential as well as commercial

Industry/Entity Type

Trade

Requirements
Must have
• Need the round images to create a collage. and include the text samples of what is available

```html
<!DOCTYPE html>
<html lang="en">
<head>
<meta charset="utf-8">
<title>Projected Illuminations Flyer</title>
<link href="https://fonts.googleapis.com/css2?family=Michroma&family=Montserrat:wght@400;500;600;700;800&family=Reenie+Beanie&display=swap" rel="stylesheet">
<style>
:root{
  --night:#0a0e1c;
  --sky:#36a8dc;
  --sky-soft:#a9d8ee;
  --brand-blue:#2ea9e1;
  --navy:#0f1f33;
  --ink:#111418;
  --white:#ffffff;
  --panel:rgba(20,90,140,.16);
}
*{box-sizing:border-box;margin:0;padding:0}
html,body{width:849px;height:1200px;overflow:hidden;background:var(--white)}
.flyer{
  position:relative;width:849px;height:1200px;overflow:hidden;
  font-family:"Montserrat",Arial,sans-serif;color:var(--ink);
  background:linear-gradient(180deg,var(--night) 0,#141d33 300px,#2a5f86 430px,var(--sky) 520px,#6fc0e6 700px,var(--sky-soft) 820px,#e9f5fb 930px,var(--white) 980px);
}
.hero-photo{
  position:absolute;left:0;top:0;width:849px;height:560px;
  background:
    radial-gradient(ellipse 260px 150px at 300px 260px,rgba(214,80,190,.75),transparent 70%),
    radial-gradient(ellipse 140px 110px at 560px 270px,rgba(70,100,230,.6),transparent 70%),
    radial-gradient(ellipse 120px 80px at 320px 180px,rgba(240,170,70,.55),transparent 70%),
    linear-gradient(180deg,rgba(10,14,28,.2) 0,rgba(40,110,150,.15) 75%,transparent 100%);
}
.side-panel{
  position:absolute;left:552px;top:501px;width:270px;height:390px;
  background:linear-gradient(180deg,rgba(25,95,145,.35) 0,rgba(70,160,210,.18) 60%,rgba(255,255,255,0) 100%);
}
.photo-circle{
  position:absolute;border-radius:50%;border:4px solid var(--brand-blue);
  box-shadow:0 2px 8px rgba(0,0,0,.35);
}
.photo-circle--pink{left:647px;top:175px;width:224px;height:224px;
  background:radial-gradient(circle at 45% 55%,#c04aa8,#5a2a6a 60%,#0d1224)}
.photo-circle--july{left:457px;top:267px;width:234px;height:234px;
  background:radial-gradient(circle at 50% 45%,#8a5a4a,#3a2a30 55%,#0c0f1a)}
.photo-circle--hearts{left:603px;top:350px;width:254px;height:254px;
  background:radial-gradient(circle at 45% 35%,#e0283a,#a0203c 50%,#5a2a80 80%,#2a1a40)}
.title{
  position:absolute;left:0;width:575px;text-align:center;
  font-family:"Michroma",sans-serif;font-size:40px;line-height:46px;color:var(--white);
  top:466px;text-shadow:0 2px 6px rgba(0,40,80,.45);letter-spacing:-.5px;
}
.intro{
  position:absolute;left:60px;width:435px;top:577px;text-align:center;
  font-size:14.5px;font-weight:500;line-height:21.5px;color:var(--ink);
}
.gobo-box{
  position:absolute;left:55px;top:652px;width:439px;height:151px;
  background:var(--white);border:2px solid #b9c4cc;border-radius:20px;
}
.gobo-box__text{
  margin-top:13px;text-align:center;font-size:14.5px;font-weight:500;line-height:21.5px;
}
.gobo-list{display:flex;gap:9px;justify-content:center;margin-top:10px}
.gobo{
  width:68px;height:68px;border-radius:50%;background:#050505;
  display:flex;align-items:center;justify-content:center;
}
.gobo--letters{color:var(--white);font-size:9.5px;line-height:11px;text-align:center;font-weight:500}
.gobo--winter{background:radial-gradient(circle,#dfe9f4 30%,#7f9fc2 60%,#1d2f55 72%)}
.offer{position:absolute;left:60px;width:432px;text-align:center}
.offer__lead{top:820px;font-family:"Reenie Beanie",cursive;font-size:42px;color:var(--ink)}
.offer__price{top:858px;font-size:52px;font-weight:800;color:var(--brand-blue);letter-spacing:1px}
.offer__term{top:916px;font-size:19px;font-weight:700;color:var(--brand-blue);letter-spacing:.5px}
.offer__detail{top:940px;font-size:10.5px;font-weight:600;line-height:13.5px;letter-spacing:.3px}
.events{position:absolute;left:552px;width:270px;top:645px}
.events__title{
  font-family:"Michroma",sans-serif;font-weight:400;font-size:21px;line-height:24px;
  text-align:center;color:var(--navy);-webkit-text-stroke:.8px var(--navy);
}
.events__list{list-style:none;margin:12px 0 0 52px;font-size:16px;font-weight:500;line-height:20px}
.events__list li{position:relative;padding-left:24px;margin-bottom:10.5px}
.events__list li::before{content:"";position:absolute;left:0;top:8px;width:5px;height:5px;border-radius:50%;background:var(--ink)}
.brand{
  position:absolute;left:0;width:849px;top:1040px;display:flex;justify-content:center;align-items:center;gap:18px;
}
.brand__mark{width:42px;height:42px;background:var(--brand-blue)}
.brand__name{font-family:"Michroma",sans-serif;font-size:40px;color:var(--brand-blue);letter-spacing:2px}
.contact-bar{
  position:absolute;left:0;top:1146px;width:849px;height:54px;background:var(--brand-blue);
  color:var(--white);font-size:16px;font-weight:500;letter-spacing:.8px;
  display:flex;align-items:center;justify-content:center;padding-left:120px;gap:8px;
}
.contact-bar__sep{width:7px;height:7px;background:var(--white);display:inline-block}
</style>
</head>
<body>
<main class="flyer">
  <div class="hero-photo" role="img" aria-label="Night photo of a large stone house lit in pink, purple and blue with a projected gold pattern"></div>
  <div class="side-panel"></div>

  <div class="photo-circle photo-circle--pink" role="img" aria-label="House lit with pink and purple wall washers"></div>
  <div class="photo-circle photo-circle--july" role="img" aria-label="House with a projected 4th of July message"></div>
  <div class="photo-circle photo-circle--hearts" role="img" aria-label="House front covered in projected red hearts"></div>

  <h1 class="title">PROJECTED<br>ILLUMINATIONS</h1>

  <p class="intro">Illuminate a projected light design and 2 colored wall washers on the exterior or interior of your home business or special event.</p>

  <section class="gobo-box">
    <p class="gobo-box__text">Choose from many stock designs or customize<br>the image to make the design truly your own.</p>
    <div class="gobo-list">
      <div class="gobo" role="img" aria-label="Clover design sample"></div>
      <div class="gobo gobo--letters">ABCD<br>EFGHIJ<br>KLMNOPQ<br>RSTUV<br>WXYZ</div>
      <div class="gobo" role="img" aria-label="Dot pattern design sample"></div>
      <div class="gobo" role="img" aria-label="Tennis player design sample"></div>
      <div class="gobo gobo--winter" role="img" aria-label="Snowy tree custom image sample"></div>
    </div>
  </section>

  <p class="offer offer__lead">Rent it today for as low as</p>
  <p class="offer offer__price">$399</p>
  <p class="offer offer__term">FOR A ONE NIGHT RENTAL</p>
  <p class="offer offer__detail">INCLUDING ILLUMINATOR, 2 WALL WASHER,<br>INSTALLATION AND REMOVAL</p>

  <section class="events">
    <h2 class="events__title">PERFECT<br>FOR SPECIAL<br>EVENTS</h2>
    <ul class="events__list">
      <li>Parties</li>
      <li>Graduation</li>
      <li>Holidays</li>
      <li>Weddings</li>
      <li>Business<br>Promotions</li>
      <li>Anytime<br>you want to<br>celebrate</li>
    </ul>
  </section>

  <div class="brand">
    <span class="brand__mark"></span>
    <span class="brand__name">LUMENFIELD DESIGN</span>
  </div>

  <footer class="contact-bar">
    <span>CONTACT DETAILS HERE</span><span class="contact-bar__sep"></span>
    <span>PHONE</span><span class="contact-bar__sep"></span>
    <span>EMAIL</span>
  </footer>
</main>
</body>
</html>
```